Learning Habits- Teaching and Learning Policy

Hi,

The philosophy behind this Teaching and Learning Policy is to equip young people (Age 16-18) for many challenges that lies ahead. The pace of technological advancement is so great that it is probable that many jobs our students will do in their lifetime do not yet even exist. We realise that we need to help develop our students into effective lifelong learners – meaning that they will:

-Need to be independent whilst also being able to work as a team.
-Need to apply many different strategies to help take on new concepts.
-Reflect on current practice, and improve.

I have attached the file which has the basic designs of the 4 different leaner habits and what they entail. Each habit is colour coordinated, so please keep the colours the same.

Collaboration- Blue (royal blue)
Persevering- Red
Planning- Orange
Reflection- Yellow

I would ideally like the poster to be transferable into a powerpoint too.

Thanking you all so much.

Lenka
Updates

Project Deadline Extended Reason: Hi,I am extending this deadline as I will be requesting some changes to the title / slogan.I need the four learning habits have a catchy name which will motivate students.Please send me some suggestions.Thanking you all.Lenka Added Monday, March 28, 2016

Target Market(s)

Teachers and students (age 16-18)

Industry/Entity Type

Education

Font styles to use
Other font styles liked:
• Something friendly to kids- where the a is printed like it is written. Similar to century gothic but more friendly.

Requirements
Must have
• Laid out similar to the the website attached. Interesting, motivational yet educational to students in how they can become lifelong learners.
Nice to have
• I should be able to transfer this to a powerpoint from a poster.
• It can be four posters or one depending on the design.
Should not have
• Each Habit must be colour-coordinated:
• Collaboration- Blue (royal blue)
• Persevering- Red
• Planning- Orange
• Reflection- Yellow
• Thank you,

```html
<!DOCTYPE html>
<html lang="en">
<head>
<meta charset="utf-8">
<title>Collaboration – Learning Habit Poster</title>
<link rel="stylesheet" href="https://fonts.googleapis.com/css2?family=Teko:wght@500;600&display=swap">
<style>
  :root {
    --royal-blue: #25408f;
    --lavender: #b9bbdd;
    --paper: #ffffff;
    --backdrop: #ffffff;
    --art-grey: #b8b6b3;
  }
  html, body {
    margin: 0;
    width: 1200px;
    height: 1200px;
    overflow: hidden;
    background: var(--backdrop);
  }
  .canvas {
    width: 1200px;
    height: 1200px;
    display: flex;
    align-items: center;
    justify-content: center;
  }
  .poster {
    width: 738px;
    height: 1140px;
    display: block;
  }
  .habit-title {
    font-family: "Teko", sans-serif;
    font-weight: 600;
    font-size: 84px;
    letter-spacing: 7px;
    fill: var(--royal-blue);
  }
  .skill {
    font-family: "Teko", sans-serif;
    font-weight: 600;
    font-size: 60px;
    font-variant: small-caps;
    letter-spacing: 1px;
    text-anchor: middle;
  }
  .skill--light { fill: var(--paper); }
  .skill--soft { fill: var(--lavender); }
</style>
</head>
<body>
<main class="canvas">
  <svg class="poster" viewBox="0 0 738 1140" xmlns="http://www.w3.org/2000/svg" aria-labelledby="poster-title">
    <title id="poster-title">Collaboration learning habit poster</title>
    <defs>
      <path id="title-arc" d="M 139 365 A 230 230 0 0 1 599 365"/>
      <filter id="ring-shadow" x="-20%" y="-20%" width="140%" height="140%">
        <feDropShadow dx="0" dy="6" stdDeviation="6" flood-color="#000" flood-opacity="0.35"/>
      </filter>
    </defs>

    <rect class="poster-top" x="0" y="0" width="738" height="373" fill="var(--paper)"/>
    <rect class="poster-base" x="0" y="373" width="738" height="767" fill="var(--royal-blue)"/>

    <circle class="emblem-ring" cx="369" cy="365" r="249" fill="var(--paper)"/>
    <circle class="emblem-disc" cx="369" cy="357" r="207" fill="var(--royal-blue)"
            stroke="var(--paper)" stroke-width="4" filter="url(#ring-shadow)"/>

    <rect class="emblem-art" x="184" y="235" width="370" height="230" rx="40"
          fill="var(--art-grey)" role="img"
          aria-label="Illustration: five people holding hands with thought clouds above them"/>

    <text class="habit-title">
      <textPath href="#title-arc" startOffset="50%" text-anchor="middle">COLLABORATION</textPath>
    </text>

    <text class="skill skill--light" x="369" y="842">Empathy and Listening</text>
    <text class="skill skill--soft" x="369" y="917">Interdependence</text>
    <text class="skill skill--light" x="369" y="993">Communication</text>
    <text class="skill skill--soft" x="369" y="1069">Questioning</text>
  </svg>
</main>
</body>
</html>
```